Revamp Of Landing Page For an Automated AI Voice Agents Agency

here is my current landing page https://app.brightfunnelstudio.example/v2/preview/KXWQPmR4hLsDnTfYvJcA?notrack=true

Please use all my current content and imagery of ai agents in your new design. Make it easy to ready, easy to navigate and easy to understand

I am looking for a SLEEK shiny polished looking website. I like Dark themed sites but am open to see light themed sites too so please dont be shy.

The site should have an Ai Voice Agent Theme about it. Maybe look and feel of futureistic but simple and not intimidating to the average person...

Here are a couple website designs I like for reference:
https://q4t.example/
https://ai-bots.mervinholt.example/
https://chatvexo.example/ai-agents

Target Market(s)

b2b

Industry/Entity Type

AI Voice Agents

Coding

Coded - Design and coding required

Font styles to use
Other font styles liked:
• open

Requirements
Must have
• all elements and content and images used in existing design.
Nice to have
• open
Should not have
• open

```html
<!DOCTYPE html>
<html lang="en">
<head>
<meta charset="utf-8">
<title>Voxora – Next-Gen Voice Agents</title>
<link href="https://fonts.googleapis.com/css2?family=Poppins:wght@400;500;600;700&display=swap" rel="stylesheet">
<style>
:root{
  --navy:#0a0d2b;
  --navy-2:#12123d;
  --purple:#6a3df0;
  --violet:#8b3fe0;
  --indigo:#4f46e5;
  --yellow:#ffe500;
  --ink:#111122;
  --muted:#4a4a5e;
  --white:#ffffff;
  --line:#8a6cf0;
  --lilac:#ece6fb;
}
*{box-sizing:border-box;margin:0;padding:0}
html,body{width:1200px;height:3836px;overflow:hidden}
body{font-family:'Poppins',sans-serif;color:var(--ink);background:var(--white);position:relative}
.abs{position:absolute}
.btn{position:absolute;background:var(--yellow);color:#111;font-weight:600;font-size:11px;border-radius:4px;display:flex;align-items:center;justify-content:center;text-decoration:none}
.accent{background:linear-gradient(90deg,#6a3df0,#9b3fd8);-webkit-background-clip:text;background-clip:text;color:transparent}

/* hero + workforce */
.dark{left:0;top:0;width:1200px;height:1309px;background:
  radial-gradient(ellipse 700px 200px at 600px 160px,rgba(110,70,240,.45),transparent 70%),
  radial-gradient(ellipse 500px 400px at 1150px 500px,rgba(110,40,200,.35),transparent 70%),
  linear-gradient(180deg,#1a1448 0%,#0d0f33 35%,#0a0d2b 100%)}
.brand{font-weight:500;letter-spacing:3px;color:var(--white);font-size:22px;display:flex;align-items:center;gap:8px}
.brand .dot{width:14px;height:14px;border:2px solid var(--white);border-radius:50%}
.signup{left:1011px;top:27px;width:67px;height:22px}
.hero-title{left:0;top:118px;width:1200px;text-align:center;color:#e9e6ff;font-size:47px;font-weight:500;line-height:1.17}
.hero-card{left:122px;top:330px;width:956px;height:430px;border-radius:6px;overflow:hidden;background:linear-gradient(90deg,#7a8aa8 0%,#5b5fd8 45%,#5a3ff0 70%,#6a45ee 100%)}
.hero-photo{left:0;top:0;width:480px;height:430px;background:linear-gradient(120deg,#9aa6b8,#6e7fa8 50%,#5a60c8)}
.hero-copy{left:478px;top:76px;width:450px;color:var(--white);font-size:29px;font-weight:500;line-height:1.19}
.hero-btn{left:478px;top:316px;width:194px;height:29px}
.wf-title{left:120px;top:808px;color:var(--white);font-size:39px;font-weight:500;line-height:1.18}
.arrow{width:32px;height:32px;border:1.5px solid #cfcfe8;border-radius:50%;display:flex;align-items:center;justify-content:center}
.card{top:941px;width:226px;height:235px;border:1px solid #3c2f8a;border-radius:4px;background:linear-gradient(180deg,#0d1034,#15104a);color:var(--white);text-align:center;padding:30px 12px 0}
.card.active{background:linear-gradient(160deg,#5b4af0,#8d45d8);border-color:#7a5cf0}
.card svg{width:48px;height:48px;margin-bottom:10px}
.card h3{font-size:15px;font-weight:500;margin-bottom:6px}
.card .sub{font-size:8.5px;font-weight:600;line-height:1.3;margin-bottom:8px}
.card p{font-size:8.5px;line-height:1.3;color:#e4e2f4}
.wf-btn{left:503px;top:1216px;width:194px;height:29px}

/* wish */
.wish{left:0;top:1309px;width:1200px;height:946px;background:var(--white);overflow:hidden}
.ghost{left:0;top:16px;font-size:110px;font-weight:600;letter-spacing:10px;color:#eeebfb;line-height:1}
.person{left:737px;top:0;width:463px;height:533px;border-radius:0 0 0 100%;background:radial-gradient(circle at 60% 45%,#d9ccf6,#ebe4fb 70%)}
.person-shape{left:90px;top:60px;width:260px;height:420px;border-radius:130px 130px 20px 20px;background:linear-gradient(180deg,#e6dcd0,#cfc8c0)}
.wish-title{left:120px;top:175px;font-size:40px;font-weight:500;line-height:1.15}
.wish-title b{font-weight:700}
.wish-lead{left:120px;top:270px;font-size:19px;font-weight:500}
.wish-small{left:120px;top:316px;width:440px;font-size:11px;font-weight:500}
.wish-body{left:120px;top:352px;width:440px;font-size:11px;line-height:1.7;color:#222}
.wish-btn{left:121px;top:443px;width:196px;height:28px}
.emp-title{left:0;top:578px;width:1200px;text-align:center;font-size:40px;font-weight:500;line-height:1.2}
.emp-title b{font-weight:700}
.emp-sub{left:0;top:632px;width:1200px;text-align:center;font-size:18px;font-weight:500}
.feat{top:701px;width:306px;height:113px;border:1px solid var(--line);border-radius:3px;display:flex;align-items:center;padding-left:34px;gap:22px}
.feat .ico{width:62px;height:62px;background:var(--lilac);border-radius:4px;display:flex;align-items:center;justify-content:center}
.feat h4{font-size:15px;font-weight:500;margin-bottom:2px}
.feat p{font-size:10.5px;line-height:1.35;color:#222}
.emp-btn{left:503px;top:853px;width:194px;height:28px}

/* promise */
.promise{left:0;top:2255px;width:1200px;height:522px;background:
  radial-gradient(ellipse 300px 400px at 1080px 200px,rgba(40,140,230,.55),transparent 70%),
  linear-gradient(110deg,#1e1050 0%,#151040 45%,#0b1d4a 100%)}
.promise-face{left:900px;top:0;width:300px;height:522px;background:linear-gradient(160deg,#1c5fc0,#0b1d4a 80%)}
.promise-title{left:0;top:50px;width:1200px;text-align:center;color:var(--white);font-size:39px;font-weight:500}
.pcard{top:136px;width:325px;height:178px;border-radius:3px;background:linear-gradient(150deg,#5b47ec,#8b43d8);color:var(--white);text-align:center;display:flex;flex-direction:column;align-items:center;justify-content:center}
.pcard svg{width:52px;height:52px;margin-bottom:10px}
.pcard h4{font-size:15px;font-weight:500}
.pcard p{font-size:10.5px;line-height:1.3;margin-top:6px}
.promise-note{left:0;top:370px;width:1200px;text-align:center;color:var(--white);font-size:18px;font-weight:500;line-height:1.3}
.stars{left:532px;top:438px;display:flex;gap:4px}

/* faq */
.faq{left:0;top:2777px;width:1200px;height:466px;background:linear-gradient(180deg,#fff,#f4f1fb)}
.faq-title{left:0;top:42px;width:1200px;text-align:center;font-size:40px;font-weight:500}
.qa{left:121px;width:957px;border:1px solid #b8a3f2;border-bottom:3px solid #7d56e8;border-radius:4px;background:var(--white);padding:0 18px;display:flex;justify-content:space-between;align-items:center;font-size:15px}
.qa.open{background:linear-gradient(90deg,#5b47ec,#8d45d8);color:var(--white);align-items:flex-start;padding-top:18px;border-color:#7a5cf0}
.qa.open p{font-size:11px;line-height:1.7;margin-top:4px;color:#ece8ff;width:520px}
.plus{font-size:32px;font-weight:300;color:#5a3df0;line-height:1}
.qa.open .plus{color:var(--white)}

/* cta */
.cta{left:0;top:3243px;width:1200px;height:308px;background:linear-gradient(90deg,#0a1a36 0%,#0b1e3a 50%,#0d2d44 100%)}
.cta-art{left:700px;top:0;width:500px;height:308px;background:radial-gradient(ellipse 220px 220px at 290px 140px,rgba(40,200,210,.55),transparent 75%)}
.cta-title{left:121px;top:50px;width:600px;color:var(--white);font-size:40px;font-weight:500;line-height:1.12}
.cta-btn{left:122px;top:216px;width:195px;height:28px}

/* footer */
.footer{left:0;top:3551px;width:1200px;height:285px;background:linear-gradient(180deg,#1a1448,#0f0e33)}
.news{left:390px;top:74px;color:var(--white);font-size:19px;font-weight:500}
.email{left:586px;top:69px;width:360px;height:44px;border:1px solid #5d55a0;border-radius:4px;color:#ddd;font-size:11px;padding-left:14px;display:flex;align-items:center}
.subscribe{left:960px;top:69px;width:118px;height:44px;background:#6a3df0;color:var(--white);border-radius:4px;font-size:12px;display:flex;align-items:center;justify-content:center}
.legal{left:0;width:1200px;text-align:center;color:var(--white);font-size:10px}
</style>
</head>
<body>

<section class="abs dark">
  <div class="abs brand" style="left:121px;top:18px"><span>VOXORA</span><span class="dot"></span></div>
  <a class="btn signup">Sign up</a>
  <h1 class="abs hero-title">Next-Gen Voice Agents,<br>Powered by <span class="accent" style="background:linear-gradient(90deg,#6a5cff,#8a5cf5);-webkit-background-clip:text;background-clip:text">AI</span></h1>

  <div class="abs hero-card">
    <div class="abs hero-photo" role="img" aria-label="Humanoid robot wearing headphones in a bright office"></div>
    <p class="abs hero-copy">Ai Voice Agents That Answer Calls, Book Appts, Send Emails, Text Messages, Follow Up Reminders, Transfer Calls &amp; More For You 24 Hours 7 Days A Week!</p>
    <a class="btn hero-btn">Get An Instant Free Demo</a>
  </div>

  <h2 class="abs wf-title">Meet Your New <span style="color:#7a4af0;font-weight:600">AI-<br>Powered</span> Workforce</h2>
  <div class="abs" style="left:1003px;top:817px;display:flex;gap:10px">
    <div class="arrow"><svg width="12" height="12" viewBox="0 0 12 12"><path d="M8 2 4 6l4 4" fill="none" stroke="#fff" stroke-width="1.5"/></svg></div>
    <div class="arrow"><svg width="12" height="12" viewBox="0 0 12 12"><path d="M4 2l4 4-4 4" fill="none" stroke="#fff" stroke-width="1.5"/></svg></div>
  </div>

  <div class="abs card" style="left:121px">
    <svg viewBox="0 0 48 48" fill="none" stroke="#7a6cff" stroke-width="1.6"><path d="M14 40V30c-4-3-6-7-6-12a14 14 0 0 1 28 0l4 8h-4v6a4 4 0 0 1-4 4h-4v4"/><path d="M20 14v12M26 12v16M32 18v6"/><circle cx="20" cy="12" r="2"/><circle cx="26" cy="10" r="2"/></svg>
    <h3>Ai Sales Agent</h3>
    <p>Brian will take your inbound sales calls. Will give all detailed information to the customer, answer questions in a normal conversational tone and can book sales appointments or transfer hot prospects to a human to close the sale.</p>
  </div>
  <div class="abs card" style="left:365px">
    <svg viewBox="0 0 48 48" fill="none" stroke="#7a6cff" stroke-width="1.6"><rect x="14" y="14" width="20" height="20" rx="2"/><rect x="19" y="19" width="10" height="10"/><path d="M18 14V6M24 14V4M30 14V6M18 34v8M24 34v10M30 34v8M14 18H6M14 24H4M14 30H6M34 18h8M34 24h10M34 30h8"/></svg>
    <h3>Ai Appointment Setter</h3>
    <div class="sub">Book Appts &amp; Reservations On Auto Pilot</div>
    <p>Bobby offers business advice, helps brainstorm ideas, and provides insights on growth tactics to support your entrepreneurial journey.</p>
  </div>
  <div class="abs card active" style="left:609px">
    <svg viewBox="0 0 48 48" fill="none" stroke="#fff" stroke-width="1.6"><path d="M24 6c-6 0-10 3-11 7-4 1-6 5-5 9-2 3-1 8 3 10 1 5 6 8 13 8s12-3 13-8c4-2 5-7 3-10 1-4-1-8-5-9-1-4-5-7-11-7z"/><path d="M24 8v32M16 18h6M28 16l4 4M16 28l6 2M30 28h6"/><circle cx="16" cy="18" r="1.5"/><circle cx="32" cy="20" r="1.5"/></svg>
    <h3>Ai Lead Qualifier</h3>
    <div class="sub">Conversate With Prospects To Qualify<br>Before Handing Over To Sales Team</div>
    <p>All of our ai agents gather information and qualify leads. If they are interested in the services on the call then our ai agents will assist them with booking an appointment with our sales team over the call.</p>
  </div>
  <div class="abs card" style="left:852px">
    <svg viewBox="0 0 48 48" fill="none" stroke="#7a6cff" stroke-width="1.6"><circle cx="24" cy="26" r="12"/><path d="M24 20v6l4 3M12 14l-4-4M36 14l4-4M24 14V6M18 8h12M8 34l-4 4M40 34l4 4"/></svg>
    <h3>Ai Follow Up Reminders</h3>
    <div class="sub">Calls, Sends SMS &amp; Email Reminders</div>
    <p>Sam handles all the follow up calls, appt reminders and sends out the email and sms reminders too.</p>
  </div>
  <a class="btn wf-btn">Get An Instant Free Demo</a>
</section>

<section class="abs wish">
  <div class="abs ghost">VOXORA</div>
  <div class="abs person" role="img" aria-label="Young man with glasses working on a laptop">
    <div class="abs person-shape"></div>
  </div>
  <h2 class="abs wish-title">Your wish Is their<br><b class="accent">command</b></h2>
  <p class="abs wish-lead">Install the power of AI for your business</p>
  <p class="abs wish-small">Your New Ai Agents Will Never Call In Sick And Will Never Complain!</p>
  <p class="abs wish-body">With your new team of AI Agents, handling inbound calls, sending emails and sms messages, booking appointments and handling customer service inquiries is going to save you a ton of time and money.</p>
  <a class="btn wish-btn">Get An Instant Free Demo</a>

  <h2 class="abs emp-title">An Employee that Never Gets <b class="accent">Sick!</b></h2>
  <p class="abs emp-sub">Our Ai Agents Our Ready To Be Hired</p>

  <div class="abs feat" style="left:122px">
    <div class="ico"><svg width="34" height="34" viewBox="0 0 34 34" fill="none" stroke="#6a3df0" stroke-width="1.4"><path d="M17 4c-5 0-8 3-8 7-3 1-4 4-3 7-2 3 0 7 4 7 1 3 4 5 7 5s6-2 7-5c4 0 6-4 4-7 1-3 0-6-3-7 0-4-3-7-8-7z"/><path d="M17 6v22M11 14h4M19 18h5"/></svg></div>
    <div><h4>Trained In Seconds</h4><p>Learns Your Entire Website<br>In Seconds</p></div>
  </div>
  <div class="abs feat" style="left:447px">
    <div class="ico"><svg width="34" height="34" viewBox="0 0 34 34" fill="none" stroke="#6a3df0" stroke-width="1.4"><circle cx="17" cy="17" r="12"/><path d="M5 17h24M17 5c-4 4-4 20 0 24M17 5c4 4 4 20 0 24"/></svg></div>
    <div><h4>Worldwide</h4><p>Works Anywhere In The Globe</p></div>
  </div>
  <div class="abs feat" style="left:771px">
    <div class="ico"><svg width="34" height="34" viewBox="0 0 34 34" fill="none" stroke="#6a3df0" stroke-width="1.4"><circle cx="10" cy="10" r="4"/><circle cx="24" cy="10" r="4"/><circle cx="10" cy="24" r="4"/><circle cx="24" cy="24" r="4"/><path d="M14 10h6M14 24h6M10 14v6"/></svg></div>
    <div><h4>User-friendly</h4><p>Your Ai Agents Sound As If<br>They're Real Humans</p></div>
  </div>
  <a class="btn emp-btn">Get An Instant Free Demo</a>
</section>

<section class="abs promise">
  <div class="abs promise-face" role="img" aria-label="Glowing blue digital face in profile"></div>
  <h2 class="abs promise-title">Our <b class="accent" style="background:linear-gradient(90deg,#6a5cff,#8a5cf5);-webkit-background-clip:text;background-clip:text">Promise</b> To You:</h2>
  <div class="abs pcard" style="left:264px">
    <svg viewBox="0 0 52 52" fill="none" stroke="#fff" stroke-width="1.6"><circle cx="26" cy="26" r="14"/><path d="M10 20a17 17 0 0 1 30-6M42 32a17 17 0 0 1-30 6M40 8v6h-6M12 44v-6h6"/><path d="M30 21c-1-2-7-2-7 1s7 2 7 6-6 3-7 1M26 17v18"/></svg>
    <h4>14-day money-back guarantee*</h4>
  </div>
  <div class="abs pcard" style="left:612px">
    <svg viewBox="0 0 52 52" fill="none" stroke="#fff" stroke-width="1.6"><circle cx="26" cy="18" r="7"/><path d="M14 36c2-7 7-9 12-9s10 2 12 9M8 22a18 18 0 0 1 36 0M8 22v6h4M44 22v6h-4M10 40h32"/></svg>
    <h4>24/7 Customer Support</h4>
    <p>Often praised for our friendly<br>&amp; helpful support team</p>
  </div>
  <p class="abs promise-note">After Our Customers Have A Conversation With Their New<br>Ai Voice Agent They Give Us 5 Stars!</p>
  <div class="abs stars">
    <svg width="136" height="26" viewBox="0 0 140 26"><g fill="#ffd21f"><path id="s" d="M13 1l3.7 7.6 8.3 1.2-6 5.9 1.4 8.3L13 20l-7.4 4 1.4-8.3-6-5.9 8.3-1.2z"/><use href="#s" x="28"/><use href="#s" x="56"/><use href="#s" x="84"/><use href="#s" x="112"/></g></svg>
  </div>
</section>

<section class="abs faq">
  <h2 class="abs faq-title">Do You Have <b class="accent">Questions?</b></h2>
  <div class="abs qa" style="top:135px;height:68px"><span>What exactly are the AI Voice Agents?</span><span class="plus">+</span></div>
  <div class="abs qa open" style="top:219px;height:106px"><div><b style="font-weight:500">How will these AI Voice Agents benefit</b><p>Ai Voice Agents Answer Calls, Book Appts, Send Emails, Text Messages, Follow Up Reminders &amp; More For You 24/7!</p></div><span class="plus">+</span></div>
  <div class="abs qa" style="top:338px;height:68px"><span>Are they easy to use?</span><span class="plus">+</span></div>
</section>

<section class="abs cta">
  <div class="abs cta-art" role="img" aria-label="Woman wearing headphones with glowing neural network graphics"></div>
  <h2 class="abs cta-title">These AI Agents Can Help Your Business Tremendously. Imagine The Possibilities</h2>
  <a class="btn cta-btn">Get An Instant Free Demo</a>
</section>

<footer class="abs footer">
  <div class="abs brand" style="left:121px;top:72px;font-size:26px"><span>VOXORA</span><span class="dot"></span></div>
  <div class="abs news">Newsletter Signup</div>
  <div class="abs email">Email</div>
  <div class="abs subscribe">Subscribe</div>
  <p class="abs legal" style="top:158px">© 2025 Voxora</p>
  <p class="abs legal" style="top:182px">*14-Day Money Back Guarantee Terms: If you use the ai agents and you're not happy. Then you can contact us in the first 14 days for a full refund.</p>
  <p class="abs legal" style="top:209px;font-size:9px">PRIVACY | TERMS &amp; CONDITIONS | EARNINGS &amp; PRODUCTS DISCLAIMER</p>
</footer>

</body>
</html>
```